Letterhead Creation

I would like to create a letterhead incorporating my family crest attached. My current letterhead with my information is also attached. I would also like to add my Paralegal Marisol Dunleavy

```html
<!DOCTYPE html>
<html lang="en">
<head>
<meta charset="utf-8">
<title>Letterhead – Law Offices of Thomas R. Whitfield</title>
<link rel="stylesheet" href="https://fonts.googleapis.com/css2?family=Arimo:wght@400;700&display=swap">
<style>
  :root {
    --brand: #352f8c;
    --brand-soft: #9b98cf;
    --paper: #ffffff;
    --ink: #1a1a1a;
    --backdrop: #e9e7e3;
  }
  * { box-sizing: border-box; margin: 0; padding: 0; }
  html, body { width: 1200px; height: 800px; overflow: hidden; }
  body {
    background: var(--backdrop);
    font-family: "Arimo", Arial, sans-serif;
    display: flex; align-items: center; justify-content: center;
  }
  .letterhead {
    position: relative;
    width: 588px; height: 760px;
    background: var(--paper);
    box-shadow: 0 4px 18px rgba(0,0,0,.15);
    color: var(--ink);
    overflow: hidden;
  }
  .header-band {
    position: absolute; top: 96px; left: 0; right: 0; height: 26px;
    background: var(--brand);
  }
  .firm-name {
    position: absolute; top: 0; left: 22px; width: 200px; height: 26px;
    display: flex; align-items: center;
    color: #fff; font-size: 9px; letter-spacing: .04em; text-transform: uppercase;
    white-space: nowrap;
  }
  .crest-frame {
    position: absolute; top: 56px; left: 236px;
    width: 104px; height: 92px;
    background: #fff; border: 1.5px solid var(--brand); border-radius: 6px;
    padding: 6px;
  }
  .crest-frame .crest-art { width: 100%; height: 100%; border-radius: 3px;
    background: radial-gradient(circle at 50% 55%, #2c2770 0%, #5a55a8 55%, #e6e5f3 100%); }
  .contact {
    position: absolute; top: 60px; right: 16px; width: 218px;
    font-size: 9px; line-height: 1.3; color: #fff;
    background: var(--brand); padding: 6px 10px;
    display: grid; grid-template-columns: auto 1fr; column-gap: 6px;
    white-space: nowrap;
  }
  .crest-backdrop {
    position: absolute; top: 230px; left: 170px; width: 270px; height: 250px;
    border-radius: 40% 40% 50% 50%;
    background: radial-gradient(ellipse at 50% 60%, var(--brand-soft) 0%, rgba(155,152,207,.45) 55%, rgba(155,152,207,0) 78%);
  }
  .letter-body {
    position: absolute; top: 176px; left: 40px; right: 30px;
    font-size: 11px; line-height: 1.35; font-weight: 700;
  }
  .letter-body p { margin-bottom: 14px; }
  .letter-body .lorem { line-height: 1.5; }
  .footer-band {
    position: absolute; bottom: 22px; left: 0; right: 0; height: 24px;
    background: var(--brand);
    color: #fff; font-size: 11px;
    display: flex; align-items: center; justify-content: flex-end; padding: 0 26px;
  }
</style>
</head>
<body>
  <main class="letterhead">
    <div class="header-band">
      <span class="firm-name">Law Offices of Thomas R. Whitfield</span>
    </div>
    <div class="crest-frame">
      <div class="crest-art" role="img" aria-label="Family crest"></div>
    </div>
    <div class="contact">
      <span>Telephone:</span><span>(555) 210-4471</span>
      <span>Fax:</span><span>(555) 210-4472</span>
      <span>Email:</span><span>thomas@whitfieldlaw.example</span>
      <span>Paralegal:</span><span>Marisol Dunleavy</span>
    </div>

    <div class="crest-backdrop" role="img" aria-label="Faint family crest in the background"></div>

    <section class="letter-body">
      <p>Brightline Supply<br>Daniel Porter<br>P: 555-368-0100<br>P.O. Box 000000<br>Ridgeton, CO 80000<br>brightlinesupply.example</p>
      <p>August 28, 2011</p>
      <p>First Last Name<br>Street Address<br>City, State 00000</p>
      <p>Dear :</p>
      <p class="lorem">Lorem ipsum dolor sit amet, consectetur adipiscing elit. Aenean ut ipsum eget massa fringilla. Aliquam porta lectus nec mauris ornare venenatis. Vivamus non est turpis, et cursus lorem. Morbi imperdiet neque vehicula nunc convallis gravida. Vestibulum iaculis pretium placerat. Etiam pellentesque, velit id dapibus fermentum, turpis sapien ornare dui, ac tincidunt ligula.</p>
      <p>Sincerely,</p>
      <p>Daniel Porter<br>BrightlineSupply.example<br>P.O. Box 000000<br>Ridgeton, CO 80000<br>P: (555) 368-0100</p>
    </section>

    <div class="footer-band">
      <span class="firm-address">Thomas Whitfield Esq. 412 N. Alder Ave. Fairview, Ca 90000</span>
    </div>
  </main>
</body>
</html>
```